Antibacterial Hand Wash Squeeze Tube Label

We're looking for a contemporary label design for a new Antibacterial Hand Wash for an 8oz squeeze tube. The new consumer brand will be sold to consumers in major US retail stores & online. The moisturizing hand wash contains Aloe Vera, vitamin E, and other natural ingredients so the design should include the color green. Real photos are very effective on packaging, so a picture of Aloe Vera or possibly two hands washing would help draw consumers' attention to the tube on the retail shelf. The front label may wrap around the sides. Rear must be left mostly blank
Target Market(s)
US Consumers - retail stores & online
Industry/Entity Type
Consumer

```html
<!DOCTYPE html>
<html lang="en">
<head>
<meta charset="UTF-8">
<title>Velora Hand Wash – Tube Label</title>
<link href="https://fonts.googleapis.com/css2?family=Lilita+One&family=Roboto+Condensed:wght@500;700&display=swap" rel="stylesheet">
<style>
  :root {
    --stage: #0c1a30;
    --stage-glow: #1a2d4a;
    --label-blue: #2e8fd8;
    --label-lime: #d8e246;
    --brand-white: #ffffff;
    --brand-dot: #f4d23a;
    --shield-light: #4fb3a8;
    --shield-deep: #1d6a6a;
    --aloe-light: #a6dc7a;
    --aloe-deep: #3f9a44;
    --text-green: #2a6b35;
    --text-dark: #1d2a3a;
    --rule: #6d7f5a;
  }
  html, body {
    margin: 0;
    width: 1200px;
    height: 919px;
    overflow: hidden;
  }
  body {
    background: radial-gradient(ellipse at 50% 45%, var(--stage-glow) 0%, var(--stage) 70%);
    font-family: "Roboto Condensed", Arial, sans-serif;
    position: relative;
  }
  .label {
    position: absolute;
    left: 390px;
    top: 70px;
    width: 420px;
    height: 780px;
    overflow: hidden;
  }
  .label__ground,
  .art-shield {
    position: absolute;
    display: block;
  }
  .label__ground {
    inset: 0;
    width: 100%;
    height: 100%;
  }
  .brand {
    position: absolute;
    top: 120px;
    left: 0;
    right: 0;
    text-align: center;
  }
  .brand__name {
    display: inline-flex;
    align-items: center;
    gap: 12px;
    font-family: "Lilita One", Arial, sans-serif;
    font-size: 66px;
    line-height: 1;
    color: var(--brand-white);
  }
  .brand__dot {
    width: 22px;
    height: 22px;
    border-radius: 50%;
    background: var(--brand-dot);
  }
  .brand__product {
    margin-top: 8px;
    font-family: "Lilita One", Arial, sans-serif;
    font-size: 30px;
    line-height: 1;
    color: var(--brand-white);
    letter-spacing: 0.5px;
  }
  .art-shield {
    top: 292px;
    left: 145px;
    width: 130px;
    height: 156px;
  }
  .art-aloe {
    position: absolute;
    top: 462px;
    left: 110px;
    width: 200px;
    height: 150px;
    background: radial-gradient(ellipse 50% 50% at 50% 55%, var(--aloe-light) 0%, var(--aloe-deep) 45%, rgba(63,154,68,0.35) 72%, rgba(63,154,68,0) 100%);
  }
  .claims {
    position: absolute;
    top: 630px;
    left: 0;
    right: 0;
    text-align: center;
  }
  .claims__list {
    display: inline-block;
    border-top: 1.5px solid var(--rule);
    border-bottom: 1.5px solid var(--rule);
    padding: 6px 14px;
  }
  .claims__main {
    font-weight: 700;
    font-size: 17px;
    color: var(--text-green);
    letter-spacing: 0.3px;
  }
  .claims__sub {
    margin-top: 4px;
    padding-top: 4px;
    border-top: 1px solid var(--rule);
    font-weight: 500;
    font-size: 16px;
    color: var(--text-green);
  }
  .net-weight {
    margin-top: 16px;
    font-weight: 700;
    font-size: 14px;
    color: var(--text-dark);
  }
</style>
</head>
<body>
  <section class="label">
    <svg class="label__ground" viewBox="0 0 420 780" preserveAspectRatio="none" aria-hidden="true">
      <rect width="420" height="780" fill="var(--label-blue)"/>
      <polygon points="0,420 420,250 420,780 0,780" fill="var(--label-lime)"/>
    </svg>

    <header class="brand">
      <div class="brand__name"><span class="brand__dot"></span>Velora</div>
      <div class="brand__product">Hand Wash</div>
    </header>

    <svg class="art-shield" viewBox="0 0 130 156" role="img" aria-label="Shield emblem with hands washing under running water and a vitamin E drop">
      <defs>
        <linearGradient id="shield-fill" x1="0" y1="0" x2="0.4" y2="1">
          <stop offset="0" stop-color="var(--shield-light)"/>
          <stop offset="1" stop-color="var(--shield-deep)"/>
        </linearGradient>
      </defs>
      <path d="M65 4 L124 20 V72 C124 110 98 138 65 152 C32 138 6 110 6 72 V20 Z" fill="url(#shield-fill)"/>
    </svg>

    <div class="art-aloe" role="img" aria-label="Aloe vera plant with sliced aloe leaf pieces"></div>

    <div class="claims">
      <div class="claims__list">
        <div class="claims__main">99% ALOE VERA GEL</div>
        <div class="claims__sub">PARABEN FREE</div>
      </div>
      <div class="net-weight">NET WT 2.OZ (50g)</div>
    </div>
  </section>
</body>
</html>
```